Brightwave Business Card

Professional Business Card Design required using the attached contact information.

Contact information can be rearranged as required.

The company is a new start up venture developing solar systems, the branding should be in keeping with that of one of the investors whose website is as follows https://www.quorvex.com/

```html
<!DOCTYPE html>
<html lang="en">
<head>
<meta charset="utf-8">
<title>Brightwave Renewables Business Card</title>
<link href="https://fonts.googleapis.com/css2?family=Montserrat:wght@500&family=Oswald:wght@500&family=Roboto:wght@400&display=swap" rel="stylesheet">
<style>
  :root {
    --backdrop: #1d1d20;
    --card-light: #ffffff;
    --card-dark: #3c3c3e;
    --ink: #1a1a1a;
    --accent: #3f8fac;
    --logo-light: #ffffff;
  }
  * { margin: 0; padding: 0; box-sizing: border-box; }
  html, body {
    width: 1200px; height: 786px; overflow: hidden;
    background: var(--backdrop);
  }
  .canvas { position: relative; width: 1200px; height: 786px; }
  .card {
    position: absolute;
    width: 540px; height: 309px;
    box-shadow: 0 14px 30px rgba(0,0,0,.45);
  }
  .card--front { left: 50px; top: 120px; background: var(--card-light); }
  .card--back { left: 610px; top: 360px; background: var(--card-dark); }

  .wordmark {
    position: absolute;
    font-family: "Montserrat", sans-serif;
    font-weight: 500;
    letter-spacing: 3px;
    white-space: nowrap;
    display: flex; align-items: center; gap: 10px;
  }
  .wordmark__dot { width: 8px; height: 8px; border-radius: 50%; background: currentColor; }
  .card--front .wordmark { left: 118px; top: 52px; font-size: 20px; color: var(--ink); }
  .card--back .wordmark {
    left: 0; right: 0; top: 138px; justify-content: center;
    font-size: 25px; color: var(--logo-light);
  }

  .holder-name {
    position: absolute; left: 44px; top: 156px;
    font-family: "Oswald", sans-serif; font-weight: 500;
    font-size: 34px; letter-spacing: .5px;
    color: var(--accent); text-transform: uppercase;
  }
  .divider {
    position: absolute; left: 262px; top: 142px;
    width: 1.5px; height: 70px; background: var(--accent);
  }
  .contact-list {
    position: absolute; left: 282px; top: 142px;
    list-style: none;
    font-family: "Roboto", sans-serif; font-size: 12.5px; color: var(--ink);
  }
  .contact-list li { display: flex; align-items: center; gap: 7px; height: 20px; }
  .contact-list svg { width: 10px; height: 10px; flex: none; }
  .address {
    position: absolute; left: 0; right: 30px; bottom: 38px; text-align: right;
    font-family: "Roboto", sans-serif; font-size: 12.5px; color: var(--ink);
  }
</style>
</head>
<body>
<main class="canvas">
  <section class="card card--front" aria-label="Business card front">
    <div class="wordmark"><span>BRIGHTWAVE RENEWABLES</span><span class="wordmark__dot"></span></div>
    <h1 class="holder-name">Daniel Hollis</h1>
    <div class="divider"></div>
    <ul class="contact-list">
      <li>
        <svg viewBox="0 0 10 10" aria-hidden="true"><path d="M2 0.8 L3.6 2.6 L2.8 3.6 C3.4 5 4.8 6.4 6.2 7 L7.2 6.2 L9 7.8 L7.8 9.2 C4.4 8.8 1 5.4 0.6 2 Z" fill="var(--accent)"/></svg>
        <span>+1 (555) 014-2276</span>
      </li>
      <li>
        <svg viewBox="0 0 10 10" aria-hidden="true"><rect x="0.6" y="2" width="8.8" height="6" fill="none" stroke="var(--accent)" stroke-width="1"/><path d="M0.6 2 L5 5.4 L9.4 2" fill="none" stroke="var(--accent)" stroke-width="1"/></svg>
        <span>daniel.hollis@brightwave-renewables.com</span>
      </li>
      <li>
        <svg viewBox="0 0 10 10" aria-hidden="true"><circle cx="5" cy="5" r="4.3" fill="none" stroke="var(--accent)" stroke-width="1"/><ellipse cx="5" cy="5" rx="1.8" ry="4.3" fill="none" stroke="var(--accent)" stroke-width=".8"/><path d="M0.7 5 H9.3" stroke="var(--accent)" stroke-width=".8"/></svg>
        <span>www.brightwave-renewables.com</span>
      </li>
    </ul>
    <p class="address">218 Harbor Street, Portland, ME 04101</p>
  </section>

  <section class="card card--back" aria-label="Business card back">
    <div class="wordmark"><span>BRIGHTWAVE RENEWABLES</span><span class="wordmark__dot"></span></div>
  </section>
</main>
</body>
</html>
```